Harrowvane Business Card

Looking for a new business Card layout for our company, harrowvane.

Standard Business Card , Name, email, phone, website. www.harrowvane.com

```html
<!DOCTYPE html>
<html lang="en">
<head>
<meta charset="utf-8">
<title>Harrowvane Business Card</title>
<link href="https://fonts.googleapis.com/css2?family=Montserrat:wght@800&family=Arimo:wght@400;700&display=swap" rel="stylesheet">
<style>
  :root {
    --stage: #d9d9d9;
    --card: #2b2a2c;
    --edge: #3bb4df;
    --mark: #a9a9ab;
    --text: #b9b9bb;
    --rule: #8e8e90;
  }
  * { margin: 0; padding: 0; box-sizing: border-box; }
  html, body { width: 1200px; height: 1200px; overflow: hidden; }
  body {
    background: var(--stage);
    position: relative;
    font-family: "Arimo", Arial, sans-serif;
  }
  .card {
    position: absolute;
    left: 180px;
    width: 840px;
    height: 480px;
    background: var(--card);
    border-bottom: 12px solid var(--edge);
    box-shadow: 0 14px 30px rgba(0,0,0,0.25);
    overflow: hidden;
  }
  .card--back { top: 80px; }
  .card--front { top: 640px; }

  .brand-dot {
    display: block;
    width: 78px; height: 78px;
    border-radius: 50%;
    background: var(--mark);
  }
  .brand-name {
    font-family: "Montserrat", Arial, sans-serif;
    font-weight: 800;
    color: var(--mark);
    letter-spacing: 1px;
    text-transform: uppercase;
    line-height: 1;
  }

  /* front */
  .card--front .brand {
    position: absolute;
    inset: 0;
    display: flex;
    flex-direction: column;
    align-items: center;
    justify-content: center;
    gap: 34px;
    padding-bottom: 12px;
  }
  .card--front .brand-name { font-size: 74px; }

  /* back */
  .card--back .brand-dot {
    position: absolute;
    left: 96px; top: 66px;
    width: 56px; height: 56px;
  }
  .card--back .brand-name {
    position: absolute;
    left: 60px; top: 140px;
    font-size: 44px;
  }
  .back-rule {
    position: absolute;
    left: 60px; right: 40px; top: 212px;
    height: 2px;
    background: var(--rule);
  }
  .website {
    position: absolute;
    right: 40px; top: 226px;
    font-size: 17px;
    color: var(--text);
    letter-spacing: 0.5px;
  }
  .contact {
    position: absolute;
    left: 60px; top: 282px;
    color: var(--text);
  }
  .contact-name { font-size: 28px; font-weight: 700; line-height: 1.1; }
  .contact-title { font-size: 20px; margin-top: 2px; }
  .contact-rule { width: 210px; height: 2px; background: var(--rule); margin: 14px 0 14px; }
  .contact-line {
    display: flex; align-items: center; gap: 14px;
    font-size: 19px; margin-bottom: 10px;
  }
  .contact-line svg { width: 20px; height: 20px; fill: none; stroke: var(--text); stroke-width: 1.8; }
</style>
</head>
<body>
  <section class="card card--back" aria-label="Business card back">
    <span class="brand-dot"></span>
    <div class="brand-name">Harrowvane</div>
    <div class="back-rule"></div>
    <div class="website">www.harrowvane.com</div>
    <div class="contact">
      <div class="contact-name">Marcus Hale</div>
      <div class="contact-title">President</div>
      <div class="contact-rule"></div>
      <div class="contact-line">
        <svg viewBox="0 0 24 24"><path d="M5 3h4l2 5-3 2a12 12 0 0 0 6 6l2-3 5 2v4a2 2 0 0 1-2 2A18 18 0 0 1 3 5a2 2 0 0 1 2-2z"/></svg>
        <span>555-218-4470</span>
      </div>
      <div class="contact-line">
        <svg viewBox="0 0 24 24"><rect x="3" y="5" width="18" height="14" rx="1"/><path d="M3 6l9 7 9-7"/></svg>
        <span>info@harrowvane.com</span>
      </div>
    </div>
  </section>

  <section class="card card--front" aria-label="Business card front">
    <div class="brand">
      <span class="brand-dot"></span>
      <div class="brand-name">Harrowvane</div>
    </div>
  </section>
</body>
</html>
```